Thai Restaurant Billboard Design

Design a billboard promoting food delivery during this Coronavirus time. We want to grab attention by embracing the Coronavirus and offering food delivery. People are sitting at home and this is the right time to promote food delivery.

I have the logo and spec sheet attached.

Target Market(s)

Anyone.

Requirements
Must have
• Top Heading should be big and bold:

Coronavirus Got You Quarantined?

Then put under

We Deliver
Healthy Thai Food!
Put the logo that is attached
408-231-7464
Nice to have
• Eyecatching. Creative.
Should not have
• Don't have any not haves. Make it look good.

```html
<!DOCTYPE html>
<html lang="en">
<head>
<meta charset="utf-8">
<title>Lanna Orchid House – Delivery Billboard</title>
<link rel="stylesheet" href="https://fonts.googleapis.com/css2?family=Oswald:wght@500;600;700&display=swap">
<style>
  :root {
    --sun-yellow: #f1c31f;
    --deep-teal: #1d363c;
    --brick-red: #9a1d16;
    --ink: #262424;
    --gold-text: #f2c21b;
    --white: #ffffff;
    --frame: #8a8a8a;
    --scene-warm: #e9a23b;
    --scene-teal: #2f5a5e;
  }
  html, body {
    margin: 0;
    padding: 0;
    overflow: hidden;
    background: #ffffff;
  }
  .billboard {
    position: relative;
    width: 1200px;
    height: 413px;
    overflow: hidden;
    font-family: "Oswald", "Arial Narrow", sans-serif;
  }
  .billboard__backdrop {
    position: absolute;
    inset: 0;
  }
  .billboard__frame {
    position: absolute;
    left: 10px;
    top: 10px;
    width: 1180px;
    height: 393px;
    border: 1px solid var(--frame);
    box-sizing: border-box;
    pointer-events: none;
  }
  .headline {
    position: absolute;
    left: 60px;
    top: 52px;
    margin: 0;
    font-size: 52px;
    line-height: 56px;
    font-weight: 700;
    color: var(--ink);
    letter-spacing: 0.2px;
  }
  .tagline {
    position: absolute;
    left: 60px;
    top: 246px;
    margin: 0;
    font-size: 25px;
    line-height: 31px;
    font-weight: 600;
    color: var(--brick-red);
  }
  .brand {
    position: absolute;
    left: 800px;
    width: 340px;
    top: 150px;
    text-align: center;
    color: var(--white);
    font-weight: 500;
  }
  .brand__mark {
    display: block;
    width: 26px;
    height: 26px;
    margin: 0 auto 16px;
    background: var(--white);
  }
  .brand__name {
    display: block;
    font-size: 26px;
    line-height: 30px;
    letter-spacing: 0.5px;
  }
  .brand__kind {
    display: block;
    font-size: 15px;
    line-height: 20px;
    letter-spacing: 1px;
  }
  .offer {
    position: absolute;
    left: 800px;
    width: 340px;
    top: 258px;
    margin: 0;
    text-align: center;
    color: var(--gold-text);
    font-size: 29px;
    line-height: 37px;
    font-weight: 600;
  }
  .phone {
    position: absolute;
    left: 800px;
    width: 340px;
    top: 336px;
    margin: 0;
    text-align: center;
    color: var(--gold-text);
    font-size: 34px;
    line-height: 44px;
    font-weight: 500;
    letter-spacing: 0.5px;
  }
</style>
</head>
<body>
<main class="billboard">
  <svg class="billboard__backdrop" width="1200" height="413" viewBox="0 0 1200 413" aria-hidden="true">
    <defs>
      <linearGradient id="sceneTone" x1="0" y1="0" x2="1" y2="1">
        <stop offset="0" stop-color="var(--scene-teal)"/>
        <stop offset="0.5" stop-color="var(--scene-warm)"/>
        <stop offset="1" stop-color="var(--scene-teal)"/>
      </linearGradient>
    </defs>
    <rect class="panel-yellow" x="0" y="0" width="420" height="413" fill="var(--sun-yellow)"/>
    <polygon class="panel-teal" points="720,0 1200,0 1200,413 685,413" fill="var(--deep-teal)"/>
  </svg>
  <svg class="billboard__backdrop" width="1200" height="413" viewBox="0 0 1200 413"
       role="img" aria-label="Illustration of a masked delivery man in a red cap holding a food box at an open doorway">
    <polygon points="412,0 722,0 687,413 378,413" fill="url(#sceneTone)"/>
  </svg>

  <h1 class="headline">Coronavirus<br>Got You<br>Quarantined?</h1>
  <p class="tagline">Thai foods boosts<br>immunity to fight<br>against Corona</p>

  <div class="brand">
    <span class="brand__mark"></span>
    <span class="brand__name">Lanna Orchid House</span>
    <span class="brand__kind">Restaurant</span>
  </div>

  <p class="offer">We Deliver<br>Healthy Thai Food!</p>
  <p class="phone">408-231-7464</p>

  <div class="billboard__frame"></div>
</main>
</body>
</html>
```